Bref créative
Stationary & Business card for Eye Dr
Brevardi Sight Care
Professional
Marcus L Brevardi, OD
487-K Oak Ridge Rd
Scotts Valley, Ca 95081
docmarcb@linkwell.net
www.optiquest-drbrevardi.com
Please incorporate the following statement into the design:
"Extraordinary eye wear
exemplary eye care"
to have logo only

```html
<!DOCTYPE html>
<html lang="en">
<head>
<meta charset="utf-8">
<title>Brevardi Sight Care – Business Card</title>
<link rel="stylesheet" href="https://fonts.googleapis.com/css2?family=Cinzel:wght@400;600&display=swap">
<style>
  :root {
    --backdrop: #d9d6d1;
    --card: #fbfbfa;
    --gold: #b8912a;
    --gold-light: #dcc06a;
    --gold-dark: #93701a;
    --ink: #3b3a37;
    --band-text: #fffaf0;
    --faint: #efe6cc;
  }
  * { margin: 0; padding: 0; box-sizing: border-box; }
  html, body {
    width: 1200px; height: 901px; overflow: hidden;
    background: var(--backdrop);
    font-family: "Cinzel", "Times New Roman", serif;
  }
  .canvas {
    position: relative; width: 1200px; height: 901px;
    display: flex; flex-direction: column; align-items: center; justify-content: center; gap: 40px;
  }
  .card {
    position: relative; width: 680px; height: 388px;
    background: var(--card);
    box-shadow: 0 6px 18px rgba(0,0,0,.18);
    overflow: hidden;
  }
  /* Back of card */
  .card-back .brand-lockup {
    position: absolute; left: 0; right: 0; top: 150px;
    display: flex; align-items: center; justify-content: center; gap: 18px;
  }
  .brand-mark-circle {
    width: 58px; height: 58px; border-radius: 50%;
    border: 2px solid var(--gold-light);
  }
  .brand-name {
    color: var(--gold); font-weight: 600; font-size: 34px; letter-spacing: 1px;
  }
  /* Front of card */
  .card-front .brand-name {
    position: absolute; left: 34px; top: 92px; font-size: 27px;
  }
  .tagline {
    position: absolute; left: 388px; top: 96px;
    color: var(--ink); font-size: 12px; line-height: 16px; letter-spacing: .6px;
  }
  .gold-band { position: absolute; left: 0; top: 0; }
  .doctor-name {
    position: absolute; left: 34px; top: 190px;
    color: var(--band-text); font-size: 20px; letter-spacing: 1px;
  }
  .address {
    position: absolute; left: 34px; top: 246px;
    color: var(--ink); font-size: 15px; line-height: 20px;
  }
  .contact-list {
    position: absolute; left: 34px; top: 300px; list-style: none;
    color: var(--ink); font-size: 14px; line-height: 20px;
  }
  .contact-list .label { color: var(--gold); font-weight: 600; }
  .website {
    position: absolute; right: 36px; top: 204px;
    color: var(--gold); font-size: 13px; letter-spacing: .4px;
  }
  .faint-circle {
    position: absolute; right: 100px; top: 250px;
    width: 84px; height: 84px; border-radius: 50%;
    border: 2px solid var(--faint);
  }
</style>
</head>
<body>
<main class="canvas">
  <section class="card card-back" aria-label="Card back">
    <div class="brand-lockup">
      <span class="brand-mark-circle"></span>
      <span class="brand-name">Brevardi Sight Care</span>
    </div>
  </section>

  <section class="card card-front" aria-label="Card front">
    <span class="faint-circle"></span>
    <svg class="gold-band" width="680" height="388" viewBox="0 0 680 388" aria-hidden="true">
      <defs>
        <linearGradient id="bandGold" x1="0" y1="0" x2="1" y2="0">
          <stop offset="0" stop-color="#93701a"/>
          <stop offset=".5" stop-color="#dcc06a"/>
          <stop offset="1" stop-color="#b8912a"/>
        </linearGradient>
      </defs>
      <polygon points="0,178 380,178 410,148 680,148 680,166 420,166 390,222 0,222" fill="url(#bandGold)"/>
    </svg>
    <span class="brand-name">Brevardi Sight Care</span>
    <p class="tagline">Extraordinary<br>eye wear &amp; exemplary eye care</p>
    <p class="doctor-name">Marcus L Brevardi, OD</p>
    <p class="address">487-K Oak Ridge Rd<br>Pine Hollow, Ca 95081</p>
    <ul class="contact-list">
      <li><span class="label">P</span> - 831-555-0148</li>
      <li><span class="label">F</span> - 831-555-0172</li>
      <li><span class="label">E</span> - docmarcb@linkwell.net</li>
    </ul>
    <p class="website">www.optiquest-drbrevardi.com</p>
  </section>
</main>
</body>
</html>
```